Skincare at Your Door Logo and business card

We provide dermatological services to the community. This includes Assisted Living Facilities, nursing homes and to large cooperation, Health fairs etc. We provide a health care provider that travels to institutions, providing these services. All procedures and surgeries are done onsite in one of our state of the art mobile clinics. We provide services including, but not limited to; skin biopsies, skin surgeries , surgical procedures including skin cancer removal mole removal and treatment of various skin disorders. we bring mobile Dermatology to you.

Industry/Entity Type

Business

Contact Information for Business Card

Need Logo address phone number, email website

Logo Text

Skincare at Your Door

Logo styles of interest
Emblem Logo
Abstract Logo
Character Logo
Lettermark Logo
Requirements
Must have
• Marcus Hadley ARNP DN-C
• Medical Facilitator
• P. (512) 384-9051
• Fax (619) 532-7140

```html
<!DOCTYPE html>
<html lang="en">
<head>
<meta charset="utf-8">
<title>Skincare at Your Door – Business Card</title>
<link rel="stylesheet" href="https://fonts.googleapis.com/css2?family=Arimo:wght@400&family=Didact+Gothic&display=swap">
<style>
  :root {
    --teal: #0f6460;
    --teal-light: #3f8a86;
    --orange: #f4a21c;
    --white: #ffffff;
    --paper: #ffffff;
  }
  * { margin: 0; padding: 0; box-sizing: border-box; }
  html, body {
    width: 1200px;
    height: 720px;
    overflow: hidden;
    background: var(--paper);
  }
  .card {
    position: relative;
    width: 1200px;
    height: 720px;
    background: var(--paper);
  }
  .brand {
    position: absolute;
    left: 0;
    top: 180px;
    width: 1200px;
    display: flex;
    justify-content: center;
    align-items: center;
    gap: 26px;
  }
  .brand-mark {
    width: 92px;
    height: 92px;
    border-radius: 50%;
    background: var(--orange);
    flex: none;
  }
  .brand-name {
    font-family: "Didact Gothic", "Century Gothic", sans-serif;
    font-size: 60px;
    font-weight: 400;
    color: var(--teal);
    letter-spacing: 0.5px;
    white-space: nowrap;
  }
  .contact-band {
    position: absolute;
    left: 40px;
    top: 430px;
    width: 1122px;
    height: 240px;
    background: var(--teal);
    overflow: hidden;
  }
  .band-texture {
    position: absolute;
    inset: 0;
    background:
      radial-gradient(circle at 30% 40%, rgba(255,255,255,0.10), rgba(255,255,255,0) 22%),
      radial-gradient(circle at 56% 55%, rgba(255,255,255,0.12), rgba(255,255,255,0) 20%),
      radial-gradient(circle at 75% 70%, rgba(255,255,255,0.08), rgba(255,255,255,0) 18%);
  }
  .person {
    position: absolute;
    left: 92px;
    top: 60px;
    width: 320px;
    text-align: center;
    color: var(--white);
    font-family: "Arimo", Arial, sans-serif;
  }
  .person-name {
    font-size: 42px;
    letter-spacing: 1.5px;
    line-height: 1;
    white-space: nowrap;
  }
  .person-credentials {
    margin-top: 12px;
    font-size: 21px;
    letter-spacing: 1px;
    line-height: 1;
  }
  .person-title {
    margin-top: 13px;
    font-size: 25px;
    letter-spacing: 3px;
    line-height: 1;
    white-space: nowrap;
  }
  .phones {
    position: absolute;
    left: 650px;
    top: 68px;
    width: 420px;
    text-align: center;
    color: var(--white);
    font-family: "Arimo", Arial, sans-serif;
    font-size: 32px;
    letter-spacing: 2px;
    line-height: 1;
  }
  .phones p + p { margin-top: 24px; }
</style>
</head>
<body>
  <main class="card">
    <header class="brand">
      <span class="brand-mark"></span>
      <span class="brand-name">Skincare at Your Door</span>
    </header>

    <section class="contact-band">
      <div class="band-texture" role="img" aria-label="Soft translucent bubble texture across the band"></div>
      <div class="person">
        <p class="person-name">MARCUS HADLEY</p>
        <p class="person-credentials">ARNP DN-C</p>
        <p class="person-title">MEDICAL FACILITATOR</p>
      </div>
      <div class="phones">
        <p class="phone">P. (512) 384-9051</p>
        <p class="fax">Fax (619) 532-7140</p>
      </div>
    </section>
  </main>
</body>
</html>
```